Logo and Website Design for KR.DN Horizont - a Software Engineering and IT company

Software engineering and IT are two different disciplines - and yet inseparably linked. At KR.DN Horizont, we combine both worlds and ensure that our software solutions are not only innovative and powerful, but also integrate perfectly into existing IT landscapes. Vision stands more for imagination, so it is not neccessary something what has to do with visualisation. Please consider that the winning competitor is also instructed to make a logo for the company. So please make a suitable logo for KR.DN Horizont to which the website fits to and show it during the website creation process. A good Logo desing is important for winning the competition. The website should contain a landing page with inspiring, perhaps futuristic photos of a datacenter and lines of code. Eventuelly flewent integrated in the text. On the landing page the company should introduced with a small text (max 250 words) followed by a section with a short text to one of our products nearby a graphic visualising the architecture of the product. The menue should be on top and fixed during scrolling and consist of the menue items home, solutions, who are we and a contact button. There should be a footer for linking social media, rights and Impressum. Only as an idea not a must. The very first view on the landing page could also be the menue bar and below of it a transparent unsharp photo (e.g. datacenter, lines of code, both ;) with the company name in the center.

###############################################################

Hi Designers,

Despite your very good approaches for describing KR.DN Horizont, here a short introduction (german text) from ourself:

------
KR.DN Horizont – Ihr Partner für ganzheitliche Softwarelösungen

Die KR.DN Horizont ist ein dynamisches Unternehmen, das sich nicht nur auf die Konzeption, das Design und die Entwicklung maßgeschneiderter Software spezialisiert hat, sondern auch deren reibungslosen Betrieb sicherstellt. Mit einem Team aus erfahrenen Softwarearchitekten und IT-Professionals verbinden wir modernste Softwareentwicklung mit tiefgehendem IT-Know-how – für Lösungen, die nachhaltig, leistungsstark und zukunftssicher sind.

Software Engineering trifft IT – Perfektion in Kombination
Software Engineering und IT sind zwei unterschiedliche Disziplinen – und doch untrennbar miteinander verbunden. Wir bei KR.DN Horizont vereinen beide Welten und sorgen dafür, dass unsere Softwarelösungen nicht nur innovativ und leistungsfähig sind, sondern sich auch perfekt in bestehende IT-Landschaften integrieren.

Expertise mit Fokus auf Healthcare & komplexe IT-Umgebungen
Unsere Experten bringen jahrzehntelange Erfahrung aus dem Healthcare-Sektor mit und unterstützen IT-Abteilungen großer Kliniken in der Entwicklung und Optimierung von Softwarelösungen. Von Anwendungssoftware bis hin zu Steuerungssystemen – unsere Softwareingenieure wissen genau, worauf es ankommt.

Ganzheitlicher Ansatz – über die Software hinaus
Wir entwickeln nicht nur Software, sondern übernehmen auch die Verantwortung für deren stabile und effiziente Betriebsumgebung. Egal, ob on-premises, in der Cloud oder als SaaS-Lösung – wir kümmern uns um den kompletten Lifecycle Ihrer Anwendung.

Ihre Vision – unsere Mission.
Ob Neuentwicklung einer SaaS-Anwendung oder die Migration bestehender Lösungen in eine moderne SaaS-Umgebung – mit KR.DN Horizont haben Sie einen starken Partner an Ihrer Seite.

Lassen Sie uns gemeinsam die Zukunft Ihrer Software gestalten!
--------------

Our first solution called "Clear Record Transfer Gateway" (CLARG)
-------------------
Teilen Sie Ihre Daten sicher – ohne Kompromisse!

Sie nutzen eine relationale Datenbank (Veltrix, Bravo Store, Quillbase etc.) und möchten ausgewählte Daten mit Dritten teilen – sei es für ein Data Warehouse, Business Controller, Lieferanten oder Kunden? Doch dabei sollen Datensicherheit, Integrität und Verfügbarkeit Ihrer primären Lösung in keiner Weise gefährdet werden?

Mit unserer Lösung erhalten Sie genau das: Maximalen Schutz für Ihre Anwendung bei gleichzeitigem Nutzen durch autorisierte Dritte – ganz ohne teure Lizenzkosten für eine Schattendatenbank.

Lassen Sie uns gemeinsam herausfinden, wie Sie Ihre Daten sicher und effizient nutzen können. Kontaktieren Sie uns – wir zeigen Ihnen, was möglich ist!
---------------------

Our second solution PLUM:
---------------------
PLUM – Program for a Tone Verification Instrument ist die smarte Lösung für Unternehmen, die bei Farbgenauigkeit keine Kompromisse machen. Die Software erkennt Farbabweichungen zwischen Mustern vollautomatisch, beschreibt sie verständlich und sorgt so für gleichbleibend hohe Produktqualität – schnell, visuell und präzise. Perfekt für alle, die Farbe zur Vertrauenssache machen.
-------------------------

Thanks,
Matthias

Target Market(s)

IT Professionals from any sector

Industry/Entity Type

Healthcare and other

Coding

Coded - Design and coding required

Number of Pages Required

1 page

Font styles to use
Sans Serif

Colors
0054AA
0677BA
7BADD7
CADEEF
E8F1F8
0094D4
00A9DD
6FCCEA
C7EBF8
E9F6FB
00AB8E
00BBA5
67D7C9
C6EFE9
E9F9F6

Requirements
Must have
• Please see description
Nice to have
• On the landing page the company should introduced with a small text (max 250 words) followed by a section with a short text to one of our products nearby a graphic visualising the architecture of the product. The menue should be on top and fixed during scrolling and consist of the menue items home, solutions, who are we and a contact button. There should be a footer for linking social media, rights and Impressum. Only as an idea not a must. The very first view on the landing page could also be the menue bar and below of it a transparent unsharp photo (e.g. datacenter, lines of code, both ;) with the company name in the center.
Should not have
• Please see description

```html
<!DOCTYPE html>
<html lang="de">
<head>
<meta charset="utf-8">
<title>KR.DN Horizont – Softwarelösungen</title>
<link rel="stylesheet" href="https://fonts.googleapis.com/css2?family=Montserrat:wght@800&family=Source+Sans+3:wght@400;600;700&display=swap">
<style>
:root{
  --blue-deep:#0054AA;
  --blue:#0677BA;
  --blue-pale:#E8F1F8;
  --green:#00AB8E;
  --green-soft:#67D7C9;
  --navy:#020B1E;
  --ink:#111;
  --white:#fff;
}
*{margin:0;padding:0;box-sizing:border-box}
html,body{width:1200px;height:3033px;overflow:hidden}
body{position:relative;background:var(--white);font-family:"Source Sans 3",Arial,sans-serif;color:var(--ink)}
.abs{position:absolute}
.btn{position:absolute;height:35px;border-radius:18px;background:var(--green);color:var(--white);font-size:14px;display:flex;align-items:center;justify-content:center;padding:0 16px}
.btn--blue{background:var(--blue-deep)}

/* top */
.topbar{left:0;top:0;width:1200px;height:35px;background:var(--blue-pale);font-size:13.5px}
.topbar .item{position:absolute;top:9px;display:flex;align-items:center;gap:8px}
.navbar{left:0;top:35px;width:1200px;height:75px;background:var(--white)}
.nav-link{position:absolute;top:28px;font-size:14px}
.nav-link.is-active{color:var(--green)}
.brand-tab{left:548px;top:-18px;width:104px;height:104px;border-radius:50%;background:var(--white)}
.brand-mark{left:574px;top:8px;width:52px;height:52px;border-radius:50%;background:var(--blue)}
.brand-name{left:0;width:1200px;text-align:center;font-weight:700;color:var(--blue-deep);font-size:29px}

/* hero */
.hero{left:0;top:110px;width:1200px;height:545px;background:radial-gradient(ellipse 70% 45% at 50% 85%,#5a37c8 0%,#1d4fb8 35%,transparent 70%),linear-gradient(180deg,#01040f 0%,#0a2756 45%,#0d3b8e 75%,#1436a0 100%)}
.hero-title{left:0;top:190px;width:1200px;text-align:center;font-family:Montserrat,Arial,sans-serif;font-weight:800;font-size:40px;line-height:51px;color:var(--white)}

/* about */
.photo{border-radius:50%}
.about-photo{left:141px;top:765px;width:406px;height:406px;background:radial-gradient(circle at 60% 40%,#6b5a48 0%,#2c2f35 45%,#0d1320 100%)}
.about-title{left:650px;top:826px;width:440px;font-size:28px;line-height:36px;font-weight:700}
.about-title .brand-inline{color:var(--blue-deep)}
.text{font-size:13.5px;line-height:24px;text-align:justify}
.about-text{left:650px;top:916px;width:408px}

/* products */
.products-bg{left:0;top:1180px;width:1200px;height:1120px;background:var(--blue-pale);
  -webkit-mask-image:linear-gradient(180deg,transparent 0,#000 120px,#000 960px,transparent 1120px);
  mask-image:linear-gradient(180deg,transparent 0,#000 120px,#000 960px,transparent 1120px)}
.products-grid{left:0;top:1180px;width:1200px;height:1120px;
  background-image:linear-gradient(rgba(255,255,255,.7) 1px,transparent 1px),linear-gradient(90deg,rgba(255,255,255,.7) 1px,transparent 1px);
  background-size:36px 36px;
  -webkit-mask-image:linear-gradient(180deg,transparent 0,#000 140px,#000 940px,transparent 1120px);
  mask-image:linear-gradient(180deg,transparent 0,#000 140px,#000 940px,transparent 1120px)}
.section-title{left:0;top:1305px;width:1200px;text-align:center;font-size:28px;font-weight:600}
.section-lead{left:0;top:1357px;width:1200px;text-align:center;font-size:13.5px;line-height:20px}
.product-title{font-size:16.5px;line-height:24px;font-weight:600}
.product-text{font-size:13.5px;line-height:23px}
.product-visual--clarg{left:706px;top:1453px;width:353px;height:353px;background:radial-gradient(circle at 50% 45%,#4fd6c8 0%,#4b3fb0 35%,#2a1f78 70%,#1f1860 100%)}
.product-visual--plum{left:141px;top:1870px;width:353px;height:353px;background:radial-gradient(circle at 50% 50%,#9a5de0 0%,#5a2bb8 40%,#2f1a86 80%)}

/* cta */
.cta{left:0;top:2398px;width:1200px;height:400px;background:var(--green-soft)}
.cta-title{left:0;top:2462px;width:1200px;text-align:center;font-size:28px;line-height:43px;font-weight:700;color:#0a0f1e}

/* footer */
.footer-contact{top:2882px;display:flex;gap:12px;color:var(--white);font-size:13.5px;line-height:19px}
.divider{top:2880px;width:1px;height:42px;background:#1b2540}
.bottombar{left:0;top:2982px;width:1200px;height:51px;background:var(--blue-deep);color:var(--white);font-size:13px}
.social{position:absolute;top:12px;width:27px;height:27px;border-radius:50%;border:1.5px solid rgba(255,255,255,.8)}
</style>
</head>
<body>

<!-- top bar -->
<div class="abs topbar">
  <div class="item" style="left:141px">
    <svg width="20" height="14" viewBox="0 0 20 14"><rect x="1" y="1" width="18" height="12" fill="none" stroke="#0054AA" stroke-width="1.6"/><path d="M1 1l9 7 9-7" fill="none" stroke="#0054AA" stroke-width="1.6"/></svg>
    <span>info@krdn-horizont.de</span>
  </div>
  <div class="item" style="right:143px">
    <svg width="18" height="18" viewBox="0 0 18 18"><path d="M4 2l3 3-2 2c1 2 3 4 5 5l2-2 3 3-2 2C7 15 3 11 2 4z" fill="none" stroke="#0054AA" stroke-width="1.5"/></svg>
    <span>+00 987 654 3210</span>
  </div>
</div>

<!-- navigation -->
<nav class="abs navbar">
  <span class="nav-link is-active" style="left:290px">Startseite</span>
  <span class="nav-link" style="left:403px">Lösungen</span>
  <span class="nav-link" style="left:732px">Wer wir sind</span>
  <span class="nav-link" style="left:862px">Kontakt</span>
</nav>
<div class="abs brand-tab"></div>
<div class="abs brand-mark"></div>
<div class="abs brand-name" style="top:59px">KR.DN Horizont</div>

<!-- hero -->
<section class="abs hero" role="img" aria-label="Datenraum mit leuchtenden Codezeilen und digitaler Punktwelle"></section>
<svg class="abs" style="left:0;top:0" width="1200" height="760" viewBox="0 0 1200 760">
  <defs>
    <linearGradient id="heroArc" x1="0" x2="1"><stop offset="0" stop-color="#00BBA5"/><stop offset=".5" stop-color="#67D7C9"/><stop offset="1" stop-color="#0054AA"/></linearGradient>
  </defs>
  <path d="M0 581 Q600 729 1200 581 L1200 760 L0 760 Z" fill="#fff"/>
  <path d="M141 620 Q600 742 1059 620 Q600 716 141 620 Z" fill="url(#heroArc)"/>
</svg>
<h1 class="abs hero-title">Technik im digitalen Zeitalter<br>Gestaltung von Lösungen durch Software</h1>
<span class="btn" style="left:522px;top:424px;width:156px">Kontaktieren Sie uns</span>

<!-- about -->
<div class="abs photo about-photo" role="img" aria-label="Foto: Entwicklerin am Computer mit eingeblendeten Codezeilen"></div>
<h2 class="abs about-title"><span class="brand-inline">KR.DN Horizont</span>-Ihr Partner für ganzheitliche Softwarelösungen</h2>
<p class="abs text about-text">KR.DN Horizont ist ein dynamisches Unternehmen, das sich nicht nur auf die Konzeption, Gestaltung und Entwicklung von Individualsoftware spezialisiert hat, sondern auch für deren reibungslosen Betrieb sorgt. Mit einem Team aus erfahrenen Softwarearchitekten und IT-Profis verbinden wir modernste Softwareentwicklung mit fundiertem IT-Know-how - für Lösungen, die nachhaltig, leistungsstark und zukunftssicher sind.</p>

<!-- products -->
<div class="abs products-bg"></div>
<div class="abs products-grid"></div>
<h2 class="abs section-title">Ausgewähltes Produkt</h2>
<p class="abs section-lead">Lorem ipsum dolor sit amet, consectetuer adipiscing elit, sed diam nonummy nibh euismod<br>tincidunt ut laoreet dolore magna aliquam erat volutpat wisi enim ad minim veniam</p>

<h3 class="abs product-title" style="left:141px;top:1465px">Offene Datenaustauschschnittstelle (CLARG)</h3>
<p class="abs product-text" style="left:141px;top:1500px;width:415px">Sie verwenden eine relationale Datenbank (Veltrix, Bravo Store, Quillbase usw.) und möchten ausgewählte Daten mit Dritten teilen - sei es für ein Data Warehouse, Business Controller, Lieferanten oder Kunden? Sie wollen aber die Datensicherheit, -integrität und -verfügbarkeit Ihrer primären Lösung in keiner Weise gefährden? Mit unserer Lösung erhalten Sie genau das: maximalen Schutz für Ihre Anwendung bei gleichzeitiger Nutzung durch autorisierte Dritte - ohne die teuren Lizenzkosten für eine Schattendatenbank.<br>Lassen Sie uns gemeinsam herausfinden, wie Sie Ihre Daten sicher und effizient nutzen können.</p>
<span class="btn" style="left:141px;top:1754px;width:156px">Kontaktieren Sie uns</span>
<div class="abs photo product-visual--clarg" role="img" aria-label="Illustration: vernetzte Rechner rund um einen zentralen Datenchip"></div>

<div class="abs photo product-visual--plum" role="img" aria-label="Illustration: Laptop mit Lupe zur Prüfung von Farbmustern"></div>
<h3 class="abs product-title" style="left:650px;top:1914px;width:300px">Software zur Qualitätssicherung der Farbgenauigkeit ( PLUM)</h3>
<p class="abs product-text" style="left:650px;top:1975px;width:410px">PLUM ist die intelligente Lösung für Unternehmen, die bei der Farbgenauigkeit keine Kompromisse eingehen. Die Software erkennt automatisch Farbabweichungen zwischen Mustern, beschreibt sie eindeutig und sorgt so für eine gleichbleibend hohe Produktqualität - schnell, visuell und präzise. Perfekt für alle, die Farbe zur Vertrauenssache machen.</p>
<span class="btn" style="left:650px;top:2138px;width:156px">Kontaktieren Sie uns</span>

<!-- call to action + footer shape -->
<div class="abs cta"></div>
<h2 class="abs cta-title">Ermutigung der Besucher, sich mit Ihnen in Verbindung zu setzen, um<br>Lösungen für die sichere und effiziente Nutzung ihrer Daten zu finden.</h2>
<span class="btn btn--blue" style="left:522px;top:2564px;width:156px">Kontaktieren Sie uns</span>
<svg class="abs" style="left:0;top:2580px" width="1200" height="410" viewBox="0 2580 1200 410">
  <path d="M141 2722 Q600 2598 1059 2722 Q600 2622 141 2722 Z" fill="#0054AA"/>
  <path d="M0 2760 Q600 2606 1200 2760 L1200 2990 L0 2990 Z" fill="#020B1E"/>
</svg>

<div class="abs brand-mark" style="top:2768px;background:var(--blue-deep)"></div>
<div class="abs brand-name" style="top:2820px;color:var(--blue)">KR.DN Horizont</div>

<div class="abs footer-contact" style="left:255px">
  <svg width="32" height="34" viewBox="0 0 32 34"><path d="M16 3a8 8 0 0 1 8 8c0 6-8 14-8 14S8 17 8 11a8 8 0 0 1 8-8z" fill="none" stroke="#fff" stroke-width="1.5"/><circle cx="16" cy="11" r="3" fill="none" stroke="#fff" stroke-width="1.5"/><path d="M10 24c-5 1-8 3-8 4 0 2 6 4 14 4s14-2 14-4c0-1-3-3-8-4" fill="none" stroke="#fff" stroke-width="1.5"/></svg>
  <span>47, Lindenhof, Parkallee<br>Neustadt, NS 204718</span>
</div>
<div class="abs divider" style="left:502px"></div>
<div class="abs footer-contact" style="left:545px">
  <svg width="32" height="34" viewBox="0 0 32 34"><path d="M7 6l5 5-3 3c2 4 5 7 9 9l3-3 5 5-3 3C13 27 6 20 4 9z" fill="none" stroke="#fff" stroke-width="1.5"/><path d="M19 5a9 9 0 0 1 9 9M19 10a4 4 0 0 1 4 4" fill="none" stroke="#fff" stroke-width="1.5"/></svg>
  <span>TELEFON<br>+00 987 654 3210</span>
</div>
<div class="abs divider" style="left:735px"></div>
<div class="abs footer-contact" style="left:778px">
  <svg width="30" height="34" viewBox="0 0 30 34"><path d="M2 14l13-10 13 10v18H2z" fill="none" stroke="#fff" stroke-width="1.5"/><rect x="7" y="8" width="16" height="14" fill="none" stroke="#fff" stroke-width="1.5"/><path d="M2 14l13 10 13-10" fill="none" stroke="#fff" stroke-width="1.5"/></svg>
  <span>E-MAIL<br>info@krdn-horizont.de</span>
</div>

<footer class="abs bottombar">
  <span class="abs" style="left:141px;top:16px">© 2025 KR.DN Horizont. All Rights Reserved.</span>
  <span class="social" style="left:928px" aria-label="Soziales Netzwerk"></span>
  <span class="social" style="left:963px" aria-label="Soziales Netzwerk"></span>
  <span class="social" style="left:998px" aria-label="Soziales Netzwerk"></span>
  <span class="social" style="left:1033px" aria-label="Soziales Netzwerk"></span>
</footer>

</body>
</html>
```